Update our business cards to match our awesome new website

Need a new design for company business cards. We have recently revamped our website and would like our business cards to get a refresh too. I've uploaded the company artwork, logo, as well as the Branding Deck to better understand the look & feel of our brand. Please visit the website at bellcrestholdingsoh.com.

Industry/Entity Type

Real Estate

Contact Information for Business Card

must use the colors outlined in the Branding Deck uploaded to the site, or the colors of our logo.

Font styles to use
Other font styles liked:
• Calibri

Requirements
Must have
• Required items: Name, title, company logo, address: 217 Fennimore Ave. Suite 300, Lakeport, OH 44093, email address: glen@bellcrestholdingsOH.com, company phone 800-555-0172, cell: 216-555-0148
Nice to have
• a more simple design. not complicated
Should not have
• cartoonish characters, or whimsical writing or artwork, stay within our branding colors

```html
<!DOCTYPE html>
<html lang="en">
<head>
<meta charset="utf-8">
<title>Bellcrest Holdings – Business Card</title>
<link href="https://fonts.googleapis.com/css2?family=Poppins:wght@400;500;700&display=swap" rel="stylesheet">
<style>
  :root {
    --bg: #2b2b2b;
    --card: #ffffff;
    --ink: #1c1c1c;
    --brand-green: #4e9a3f;
    --icon-green: #7cc242;
    --brand-blue: #1f74c4;
    --brand-blue-light: #3a8fd6;
  }
  * { margin: 0; padding: 0; box-sizing: border-box; }
  html, body { width: 1200px; height: 900px; overflow: hidden; }
  body {
    background: var(--bg);
    font-family: "Poppins", sans-serif;
    color: var(--ink);
    position: relative;
  }
  .card {
    position: absolute;
    left: 250px;
    width: 700px;
    height: 400px;
    background: var(--card);
    border-radius: 26px;
    overflow: hidden;
  }
  .card--front { top: 40px; }
  .card--back { top: 470px; }

  /* Wordmark */
  .wordmark { position: absolute; text-align: center; color: var(--ink); font-weight: 500; }
  .wordmark__name { text-transform: uppercase; letter-spacing: 2px; line-height: 1; }
  .wordmark__sub { font-size: 11px; letter-spacing: 0.5px; text-align: right; margin-top: 4px; }

  .card--front .wordmark { left: 0; right: 0; top: 140px; }
  .card--front .wordmark__name { font-size: 36px; }
  .card--front .wordmark__sub { width: 520px; margin: 6px auto 0; font-size: 12px; }

  .front-band {
    position: absolute;
    left: 0; right: 0; bottom: 0;
    height: 68px;
    background: var(--brand-green);
    border-top-left-radius: 30px;
    display: flex; align-items: center; justify-content: center;
    color: #fff;
    font-size: 17px;
    letter-spacing: 0.3px;
  }

  /* Back */
  .person { position: absolute; left: 48px; top: 44px; }
  .person__name { font-size: 38px; font-weight: 700; line-height: 1.05; }
  .person__title { font-size: 15px; font-weight: 500; letter-spacing: 0.5px; margin-top: 2px; }
  .person__rule { width: 60px; height: 2px; background: var(--ink); margin-top: 10px; }

  .card--back .wordmark { right: 40px; top: 58px; }
  .card--back .wordmark__name { font-size: 26px; }

  .address {
    position: absolute; right: 40px; top: 170px;
    display: flex; gap: 10px; align-items: flex-start;
    text-align: right; font-size: 16px; line-height: 1.4;
  }

  .contacts {
    position: absolute; left: 52px; bottom: 60px;
    list-style: none; font-size: 18px; line-height: 1.55;
  }
  .contacts li { display: flex; align-items: center; gap: 14px; }
  .icon { width: 18px; height: 18px; flex: none; }

  .back-band {
    position: absolute;
    left: 110px; right: 0; bottom: 0;
    height: 30px;
    background: linear-gradient(90deg, var(--brand-blue), var(--brand-blue-light));
    border-top-left-radius: 30px;
  }
</style>
</head>
<body>

<section class="card card--front" aria-label="Business card front">
  <div class="wordmark">
    <div class="wordmark__name">Bellcrest Holdings</div>
    <div class="wordmark__sub">of Ohio, LLC</div>
  </div>
  <div class="front-band">www.bellcrestholdingsoh.com</div>
</section>

<section class="card card--back" aria-label="Business card back">
  <div class="person">
    <div class="person__name">Glen Marlow</div>
    <div class="person__title">Managing Director</div>
    <div class="person__rule"></div>
  </div>

  <div class="wordmark">
    <div class="wordmark__name">Bellcrest Holdings</div>
    <div class="wordmark__sub">of Ohio, LLC</div>
  </div>

  <div class="address">
    <div>217 Fennimore Ave. Suite 300<br>Lakeport, OH 44093</div>
    <svg class="icon" viewBox="0 0 24 24" aria-hidden="true">
      <path d="M12 2a7 7 0 0 0-7 7c0 5 7 13 7 13s7-8 7-13a7 7 0 0 0-7-7z" fill="var(--icon-green)"/>
      <circle cx="12" cy="9" r="2.6" fill="#fff"/>
    </svg>
  </div>

  <ul class="contacts">
    <li>
      <svg class="icon" viewBox="0 0 24 24" aria-hidden="true"><path d="M6.6 10.8a15 15 0 0 0 6.6 6.6l2.2-2.2a1 1 0 0 1 1-.25 11 11 0 0 0 3.6.6 1 1 0 0 1 1 1V20a1 1 0 0 1-1 1A17 17 0 0 1 3 4a1 1 0 0 1 1-1h3.5a1 1 0 0 1 1 1c0 1.25.2 2.45.6 3.6a1 1 0 0 1-.25 1z" fill="var(--icon-green)"/></svg>
      800-555-0172
    </li>
    <li>
      <svg class="icon" viewBox="0 0 24 24" aria-hidden="true"><rect x="6" y="2" width="12" height="20" rx="2" fill="none" stroke="var(--icon-green)" stroke-width="2"/><circle cx="12" cy="18" r="1.2" fill="var(--icon-green)"/></svg>
      216-555-0148
    </li>
    <li>
      <svg class="icon" viewBox="0 0 24 24" aria-hidden="true"><g fill="none" stroke="var(--icon-green)" stroke-width="1.8"><circle cx="12" cy="12" r="9"/><ellipse cx="12" cy="12" rx="4" ry="9"/><path d="M3 12h18M5 7h14M5 17h14"/></g></svg>
      bellcrestholdingsoh.com.
    </li>
    <li>
      <svg class="icon" viewBox="0 0 24 24" aria-hidden="true"><rect x="2" y="5" width="20" height="14" fill="var(--icon-green)"/><path d="M2 5l10 8 10-8" fill="none" stroke="#fff" stroke-width="1.6"/></svg>
      glen@bellcrestholdingsOH.com
    </li>
  </ul>

  <div class="back-band"></div>
</section>

</body>
</html>
```